TOLV.
RAKESH ENTERTAINMENT & MEDIA
Use specific fonts
any thing which suits with the LOGO provided
Professional
RAKESH MEHTA
MR.
D-47, NORTH PARK-II , GURGAON 122001,HARYANA, INDIA
rakesh@tolv.co.in
www.tolv.co.in
LOG IN THE CENTRE

```html
<!DOCTYPE html>
<html lang="en">
<head>
<meta charset="utf-8">
<title>TOLV. Business Cards</title>
<link href="https://fonts.googleapis.com/css2?family=Source+Sans+3:wght@400;600;700&display=swap" rel="stylesheet">
<style>
  :root {
    --page-bg: #e9eaec;
    --card-bg: #ffffff;
    --brand-blue: #1d6f9c;
    --brand-blue-light: #3a9cc8;
    --brand-dark: #2a2a2a;
    --text-grey: #555b61;
    --divider: #c9ccd0;
  }
  * { box-sizing: border-box; margin: 0; padding: 0; }
  html, body { width: 1200px; height: 852px; overflow: hidden; }
  body {
    background: var(--page-bg);
    font-family: "Source Sans 3", Arial, sans-serif;
    position: relative;
  }
  .card {
    position: absolute;
    width: 540px;
    height: 310px;
    background: var(--card-bg);
    border-radius: 22px;
    overflow: hidden;
    box-shadow: 0 6px 18px rgba(0,0,0,0.18);
  }
  .card--vertical-split { left: 70px; top: 90px; }
  .card--logo-top { left: 590px; top: 450px; }
  .swoosh { position: absolute; left: 0; top: 0; width: 540px; height: 310px; }
  .brand-name {
    font-weight: 700;
    color: var(--brand-blue);
    letter-spacing: 1px;
    display: flex;
    align-items: center;
    gap: 12px;
    line-height: 1;
  }
  .brand-mark {
    display: inline-block;
    background: var(--brand-blue);
    border-radius: 4px;
  }
  .divider { position: absolute; width: 1px; background: var(--divider); }
  .person-name {
    font-weight: 700;
    color: var(--brand-blue);
    font-size: 17px;
    letter-spacing: 0.3px;
    white-space: nowrap;
  }
  .address {
    color: var(--text-grey);
    font-size: 13.5px;
    line-height: 1.3;
    white-space: nowrap;
  }
  .contacts { list-style: none; color: var(--text-grey); font-size: 13.5px; }
  .contacts li { display: flex; align-items: center; gap: 7px; height: 19px; white-space: nowrap; }
  .contacts svg { width: 13px; height: 13px; flex: none; }

  /* card 1 */
  .card--vertical-split .brand-name { position: absolute; left: 118px; top: 134px; font-size: 48px; }
  .card--vertical-split .brand-mark { width: 30px; height: 30px; }
  .card--vertical-split .divider { left: 315px; top: 34px; height: 210px; }
  .card--vertical-split .person-name { position: absolute; left: 333px; top: 36px; }
  .card--vertical-split .address { position: absolute; left: 333px; top: 74px; }
  .card--vertical-split .contacts { position: absolute; left: 333px; top: 140px; }

  /* card 2 */
  .card--logo-top .brand-name { position: absolute; left: 248px; top: 52px; font-size: 58px; }
  .card--logo-top .brand-mark { width: 34px; height: 34px; }
  .card--logo-top .divider { left: 300px; top: 145px; height: 125px; }
  .card--logo-top .person-name { position: absolute; left: 105px; top: 160px; width: 185px; text-align: center; }
  .card--logo-top .address { position: absolute; left: 105px; top: 190px; width: 185px; text-align: center; }
  .card--logo-top .contacts { position: absolute; left: 314px; top: 150px; }
</style>
</head>
<body>

<svg width="0" height="0" style="position:absolute">
  <defs>
    <linearGradient id="swooshBlue" x1="0" y1="0" x2="1" y2="1">
      <stop offset="0" stop-color="#3a9cc8"/>
      <stop offset="1" stop-color="#14577d"/>
    </linearGradient>
    <symbol id="icon-phone" viewBox="0 0 16 16"><path d="M4 1l3 3-2 2c1 2 3 4 5 5l2-2 3 3-2 2C7 14 2 9 2 3z" fill="#1d6f9c"/></symbol>
    <symbol id="icon-mobile" viewBox="0 0 16 16"><rect x="4" y="1" width="8" height="14" rx="1.5" fill="#1d6f9c"/><rect x="5.5" y="3" width="5" height="8" fill="#fff"/></symbol>
    <symbol id="icon-fax" viewBox="0 0 16 16"><rect x="2" y="6" width="12" height="8" rx="1" fill="#1d6f9c"/><rect x="4.5" y="1.5" width="7" height="5" fill="#1d6f9c"/><rect x="5" y="9" width="6" height="2" fill="#fff"/></symbol>
    <symbol id="icon-mail" viewBox="0 0 16 16"><circle cx="8" cy="8" r="7" fill="#1d6f9c"/><text x="8" y="11.5" font-size="10" text-anchor="middle" fill="#fff" font-family="Arial, sans-serif" font-weight="700">@</text></symbol>
    <symbol id="icon-web" viewBox="0 0 16 16"><circle cx="8" cy="8" r="7" fill="#3a9cc8"/><path d="M1 8h14M8 1c-3 3-3 11 0 14M8 1c3 3 3 11 0 14" stroke="#fff" fill="none" stroke-width="1"/></symbol>
  </defs>
</svg>

<article class="card card--vertical-split">
  <svg class="swoosh" viewBox="0 0 540 310" aria-hidden="true">
    <path d="M0 40 C45 120 70 230 170 310 L0 310 Z" fill="#2a2a2a"/>
    <path d="M0 52 C40 130 60 235 150 310 L0 310 Z" fill="url(#swooshBlue)"/>
  </svg>
  <div class="brand-name"><span class="brand-mark"></span>TOLV</div>
  <div class="divider"></div>
  <h2 class="person-name">RAKESH MEHTA</h2>
  <p class="address">D-47, North Park-II ,<br>Ridgemont 482017,<br>Eastmoor, Verania</p>
  <ul class="contacts">
    <li><svg><use href="#icon-phone"/></svg>+91-124-5820317</li>
    <li><svg><use href="#icon-mobile"/></svg>+91-9876043215</li>
    <li><svg><use href="#icon-fax"/></svg>+91-124-7093862</li>
    <li><svg><use href="#icon-mail"/></svg>rakesh@tolv.co.in</li>
    <li><svg><use href="#icon-web"/></svg>www.tolv.co.in</li>
  </ul>
</article>

<article class="card card--logo-top">
  <svg class="swoosh" viewBox="0 0 540 310" aria-hidden="true">
    <path d="M0 55 C35 130 55 225 125 310 L0 310 Z" fill="#2a2a2a"/>
    <path d="M0 68 C30 140 45 230 105 310 L0 310 Z" fill="url(#swooshBlue)"/>
  </svg>
  <div class="brand-name"><span class="brand-mark"></span>TOLV</div>
  <div class="divider"></div>
  <h2 class="person-name">RAKESH MEHTA</h2>
  <p class="address">D-47, North Park-II,<br>Ridgemont 482017,<br>Eastmoor, Verania</p>
  <ul class="contacts">
    <li><svg><use href="#icon-phone"/></svg>+91-124-5820317</li>
    <li><svg><use href="#icon-mobile"/></svg>+91-9876043215</li>
    <li><svg><use href="#icon-fax"/></svg>+91-124-7093862</li>
    <li><svg><use href="#icon-mail"/></svg>rakesh@tolv.co.in</li>
    <li><svg><use href="#icon-web"/></svg>www.tolv.co.in</li>
  </ul>
</article>

</body>
</html>
```